Book Cover Design Project - Pickup and Seduction Book Cover Needed

We are a small pickup and dating company based in Sydney, Australia called Copperfield Lantern Studio.
We have almost finished our first book that will be complete and printed in the very near future.
The title of the book will be:
"Quiet Harbour: Walking Calmly Through Mornings To Find Brighter Evenings"
With "Quiet Harbour" being the book title
and
"Walking Calmly Through Mornings To Find Brighter Evenings" being the tagline.
The book is about being honest, sincere and authentic when meeting and dating women and we require a book cover that makes a great first impression and excites guys while still being very classy and stylish.
We look forward to any and all submissions and we also look forward to choosing the best one from the submissions.
The book cover size is standard 6x9
The cover needs to be for epub AND printed books.
When designing this, design random blurb words. We will add this in later
Bleed for the book is atleast .125
The book is around 250 pages in size
The author''s name is Tobias Fenwright
Any other questions, please let me know
Reason: We want more submissions!

```html
<!DOCTYPE html>
<html lang="en">
<head>
<meta charset="utf-8">
<title>Quiet Harbour – Book Cover Spread</title>
<link rel="stylesheet" href="https://fonts.googleapis.com/css2?family=Oswald:wght@600;700&family=Roboto+Condensed:wght@700&display=swap">
<style>
  :root {
    --cover-black: #231f20;
    --accent-red: #e3211d;
    --dress-red: #a32323;
    --skin-pale: #f4ecec;
    --hair-black: #141112;
    --beam-white: #ffffff;
    --ink-white: #ffffff;
    --ink-black: #1a1718;
  }
  html, body {
    margin: 0;
    padding: 0;
    width: 1200px;
    height: 865px;
    overflow: hidden;
    background: var(--cover-black);
  }
  .spread {
    position: relative;
    width: 1200px;
    height: 865px;
    background: var(--cover-black);
    overflow: hidden;
  }

  /* Back cover */
  .back-cover {
    position: absolute;
    left: 0;
    top: 0;
    width: 560px;
    height: 865px;
  }
  .blurb {
    position: absolute;
    left: 70px;
    width: 410px;
    margin: 0;
    font-family: "Roboto Condensed", "Arial Narrow", sans-serif;
    font-weight: 700;
    font-size: 16.5px;
    line-height: 22px;
    letter-spacing: -0.2px;
    color: var(--accent-red);
  }
  .blurb--1 { top: 63px; }
  .blurb--2 { top: 196px; }
  .blurb--3 { top: 328px; }
  .blurb--4 { top: 460px; }
  .back-emblem {
    position: absolute;
    left: 68px;
    top: 608px;
    width: 28px;
    height: 36px;
  }

  /* Spine */
  .spine {
    position: absolute;
    left: 568px;
    top: 0;
    width: 70px;
    height: 865px;
  }
  .spine-title {
    position: absolute;
    left: 50%;
    top: 168px;
    transform-origin: top left;
    transform: translateX(17px) rotate(90deg);
    display: flex;
    align-items: center;
    gap: 14px;
    white-space: nowrap;
    font-family: "Oswald", "Arial Narrow", sans-serif;
    font-weight: 700;
    font-size: 31px;
    line-height: 34px;
    color: var(--accent-red);
  }
  .spine-emblem {
    width: 28px;
    height: 30px;
    display: block;
  }
  .spine-author {
    position: absolute;
    left: 50%;
    top: 565px;
    margin: 0;
    transform-origin: top left;
    transform: translateX(11px) rotate(90deg);
    white-space: nowrap;
    font-family: "Oswald", "Arial Narrow", sans-serif;
    font-weight: 700;
    font-size: 18px;
    line-height: 22px;
    color: var(--ink-white);
  }

  /* Front cover */
  .front-cover {
    position: absolute;
    left: 640px;
    top: 0;
    width: 560px;
    height: 865px;
  }
  .book-title {
    position: absolute;
    left: 28px;
    top: 116px;
    margin: 0;
    font-family: "Oswald", "Arial Narrow", sans-serif;
    font-weight: 700;
    font-size: 46px;
    line-height: 56px;
    letter-spacing: 0.5px;
    color: var(--accent-red);
  }
  .book-tagline {
    position: absolute;
    left: 28px;
    top: 181px;
    margin: 0;
    font-family: "Roboto Condensed", "Arial Narrow", sans-serif;
    font-weight: 700;
    font-size: 15px;
    line-height: 20px;
    color: var(--accent-red);
  }
  .scene {
    position: absolute;
    left: 0;
    top: 0;
    width: 560px;
    height: 865px;
  }
  .front-author {
    position: absolute;
    left: 360px;
    top: 818px;
    margin: 0;
    font-family: "Oswald", "Arial Narrow", sans-serif;
    font-weight: 700;
    font-size: 17px;
    line-height: 22px;
    color: var(--ink-black);
  }
</style>
</head>
<body>
<main class="spread">

  <section class="back-cover" aria-label="Back cover">
    <p class="blurb blurb--1">The book is about being honest, sincere and authentic when meeting and dating women and we require a book cover that makes a great first impression and excites guys while still being very classy and stylish</p>
    <p class="blurb blurb--2">The book is about being honest, sincere and authentic when meeting and dating women and we require a book cover that makes a great first impression and excites guys while still being very classy and stylish</p>
    <p class="blurb blurb--3">The book is about being honest, sincere and authentic when meeting and dating women and we require a book cover that makes a great first impression and excites guys while still being very classy and stylish</p>
    <p class="blurb blurb--4">The book is about being honest, sincere and authentic when meeting and dating women and we require a book cover that makes a great first impression and excites guys while still being very classy and stylish</p>
    <svg class="back-emblem" viewBox="0 0 28 36" role="img" aria-label="Small red bitten apple emblem">
      <ellipse cx="14" cy="19" rx="13" ry="16" fill="var(--accent-red)"/>
    </svg>
  </section>

  <section class="spine" aria-label="Spine">
    <div class="spine-title">
      <span>QUIET</span>
      <svg class="spine-emblem" viewBox="0 0 28 30" role="img" aria-label="Small red apple emblem">
        <ellipse cx="14" cy="15" rx="13" ry="14" fill="var(--accent-red)"/>
      </svg>
      <span>HARBOUR</span>
    </div>
    <p class="spine-author">Tobias Fenwright</p>
  </section>

  <section class="front-cover" aria-label="Front cover">
    <svg class="scene" viewBox="0 0 560 865">
      <defs>
        <linearGradient id="womanTone" x1="0" y1="0" x2="0" y2="1">
          <stop offset="0" stop-color="var(--hair-black)"/>
          <stop offset="0.22" stop-color="#6b5f60"/>
          <stop offset="0.42" stop-color="var(--skin-pale)"/>
          <stop offset="0.55" stop-color="#d9b3b3"/>
          <stop offset="0.68" stop-color="var(--dress-red)"/>
          <stop offset="1" stop-color="var(--dress-red)"/>
        </linearGradient>
        <linearGradient id="manTone" x1="0" y1="0" x2="0" y2="1">
          <stop offset="0" stop-color="#1a1718"/>
          <stop offset="0.55" stop-color="#2a2526"/>
          <stop offset="1" stop-color="#2a2526" stop-opacity="0"/>
        </linearGradient>
      </defs>
      <polygon points="362,262 560,262 560,865 258,865 362,555"
               fill="var(--beam-white)"/>
      <rect x="392" y="288" width="130" height="500" rx="40"
            fill="url(#manTone)" role="img"
            aria-label="Illustration of a man in a suit standing in a white beam of light, casting a long shadow"/>
      <rect x="12" y="432" width="262" height="433" rx="60"
            fill="url(#womanTone)" role="img"
            aria-label="Illustration of a woman with dark hair in a red dress holding a bitten red apple"/>
    </svg>
    <h1 class="book-title">QUIET HARBOUR</h1>
    <p class="book-tagline">Walking Calmly Through Mornings To Find Brighter Evenings</p>
    <p class="front-author">Tobias Fenwright</p>
  </section>

</main>
</body>
</html>
```